Business Telephone Service Brochure

I need a brochure designed to help sell our VoIP service. The brochure needs to be clean, attention getting, professional and have 3 key areas of information (Key Features, Benefits & Service Plans). Here is an idea of what we are looking for https://www.plenvora.com/design/24930587. Need to also include how much the customer could save. See this for an example https://quarbeline.com/postcard-flyer-design/contests/voip-sales-flyer-template-replicate-attached-582913. The Service Plan section needs to allow room for two types of plans. One plan includes the phone and has a 12, 24 and 36 month option. Each term (12,24,36) will have its own monthly cost per device. The second service option is no-commitment monthly with a single per month price per device. The included features section should allow for up to 16 features to be listed. The benefits should allow for 4-6 benefits to be listed. Also include room for Logo, business address, website, phone number and email.

Target Market(s)

Small to medium business with 1-100 employees.

Industry/Entity Type

Telecommunications

Font styles to use
Serif

Colors

Designer to choose colors to be used in the design.

Requirements
Must have
• Key Feature, Benefits and Service Plans (i.e. Pricing). Company logo, phone, email and website. Must have "Save up to x%!" and catch attention.
Nice to have
• Limited colors. I am not setting a hard limit, please take the liberty to do what you feel is needed. Just keep in mind we want it to be clean, professional and attention getting without being to flashy or obnoxious.
Should not have
• Nothing busy or distracting.

```html
<!DOCTYPE html>
<html lang="en">
<head>
<meta charset="utf-8">
<title>Norvane Business Telephone Brochure</title>
<link href="https://fonts.googleapis.com/css2?family=Source+Serif+4:opsz,wght@8..60,400;8..60,600;8..60,700&display=swap" rel="stylesheet">
<style>
  :root {
    --backdrop: #8f8f8f;
    --paper: #eef5fc;
    --ink: #2b2b2b;
    --navy: #2a2f7a;
    --heading-blue: #1f6fc4;
    --sky: #8fd0ec;
    --band: #2a9ad9;
    --grey: #b3b3b3;
    --cell: #e3e3e3;
  }
  * { margin: 0; padding: 0; box-sizing: border-box; }
  html, body { width: 1200px; height: 1200px; overflow: hidden; }
  body { background: var(--backdrop); font-family: "Source Serif 4", serif; color: var(--ink); position: relative; }
  .page { position: absolute; top: 250px; width: 495px; height: 700px; background: var(--paper); overflow: hidden; }
  .page--front { left: 85px; }
  .page--back { left: 620px; }
  .page-art { position: absolute; inset: 0; width: 495px; height: 700px; }
  .brand { position: absolute; left: 230px; top: 50px; width: 265px; height: 76px; text-align: center; }
  .brand-name { font-size: 52px; font-weight: 700; color: var(--navy); line-height: 60px; letter-spacing: -0.5px; }
  .brand-tagline { font-size: 6.5px; color: #555; }
  .address { position: absolute; left: 307px; top: 300px; font-size: 11px; line-height: 14px; color: #444; }
  .address h3 { font-weight: 400; font-size: 13px; margin-bottom: 14px; }
  .section-title { position: absolute; font-weight: 700; font-size: 16px; }
  .features-title { left: 25px; top: 470px; color: var(--heading-blue); }
  .benefits-title { left: 23px; top: 250px; color: #333; font-weight: 400; }
  .bullets { position: absolute; list-style: none; font-size: 11px; line-height: 14px; }
  .bullets li::before { content: "\2022\00a0"; }
  .features-a { left: 24px; top: 512px; }
  .features-b { left: 246px; top: 511px; }
  .benefits-a { left: 23px; top: 290px; font-size: 12.5px; line-height: 16px; }
  .benefits-b { left: 297px; top: 289px; font-size: 12.5px; line-height: 16px; }
  .contact { position: absolute; left: 30px; top: 641px; font-size: 11.5px; line-height: 15px; color: #333; }
  .plans { position: absolute; left: 22px; top: 383px; border-collapse: separate; border-spacing: 6px 10px; margin: -10px -6px; font-size: 8px; }
  .plans td { background: var(--cell); height: 20px; text-align: center; vertical-align: middle; padding: 0 3px; }
  .plans .col-service { width: 195px; }
  .plans .col-month { width: 50px; }
  .plans .col-term { width: 51px; }
  .plans .col-term-wide { width: 62px; }
  .notes { position: absolute; left: 23px; top: 503px; font-size: 10px; line-height: 13px; width: 460px; }
  .notes p + p { margin-top: 13px; }
  .savings { position: absolute; left: 23px; top: 584px; font-size: 22px; font-weight: 700; color: var(--heading-blue); }
</style>
</head>
<body>

<section class="page page--front">
  <svg class="page-art" viewBox="0 0 619 876" preserveAspectRatio="none">
    <defs>
      <linearGradient id="net-front" x1="0" y1="0" x2="1" y2="1">
        <stop offset="0" stop-color="#1a5fd0"/><stop offset=".5" stop-color="#2f8fe6"/><stop offset="1" stop-color="#0d3fae"/>
      </linearGradient>
      <linearGradient id="city" x1="0" y1="0" x2="0" y2="1">
        <stop offset="0" stop-color="#e9dfe6"/><stop offset=".6" stop-color="#b9bccb"/><stop offset="1" stop-color="#5d6880"/>
      </linearGradient>
    </defs>
    <rect class="photo" x="0" y="180" width="300" height="400" fill="url(#city)" role="img" aria-label="Photo: businessman holding a glowing phone before a city skyline"/>
    <path d="M0 560 Q160 500 330 500 L330 876 L0 876 Z" fill="#1f7cd0"/>
    <path d="M0 576 Q160 514 330 512 L330 876 L0 876 Z" fill="var(--paper)"/>
    <rect x="260" y="180" width="359" height="250" fill="var(--grey)"/>
    <circle cx="462" cy="412" r="202" fill="var(--grey)" stroke="#fff" stroke-width="3"/>
    <circle cx="462" cy="412" r="190" fill="none" stroke="#fff" stroke-width="1" opacity=".6"/>
    <g role="img" aria-label="Illustration: glowing global network">
      <path d="M0 0 H619 V225 Q430 275 260 268 Q110 258 0 195 Z" fill="url(#net-front)"/>
    </g>
    <path d="M318 0 Q332 178 560 248 Q600 252 619 246 V0 Z" fill="#4aa6dc"/>
    <path d="M334 0 Q348 162 560 236 Q600 242 619 236 V0 Z" fill="var(--sky)"/>
    <rect x="284" y="61" width="335" height="95" fill="#d4ecf8" opacity=".9"/>
    <circle cx="520" cy="260" r="250" fill="none" stroke="#fff" stroke-width="1" opacity=".5"/>
    <path d="M0 784 H330 Q405 784 412 841 H300 L282 876 H0 Z" fill="var(--grey)"/>
    <path d="M300 841 H619 V872 H284 Z" fill="var(--band)"/>
  </svg>

  <div class="brand"><div class="brand-name">norvane</div><div class="brand-tagline">Internet-Telephone-Security-Networking</div></div>

  <div class="address">
    <h3>Address Info</h3>
    Norvane Internet<br>Unit 8, Lark Business Centre<br>42 Harlow St<br>Kelmford ACT 2611<br>Postal Address:<br>PO Box 57<br>Ashdale ACT 2618
  </div>

  <h2 class="section-title features-title">Key Features</h2>
  <ul class="bullets features-a">
    <li>Unlimited local and long distance calling</li><li>HD Voice</li><li>Business SMS/Text Messaging</li><li>Personal and Shared Voicemail Boxes</li><li>Audio Conferencing</li><li>Intercom</li><li>Mobile App</li>
  </ul>
  <ul class="bullets features-b">
    <li>Auto Attendant/Interactive Voice Routing</li><li>Free web or email fax</li><li>Web admin portal</li><li>Music On Hold - Customizable</li><li>Simultaneous ring / follow-me</li><li>Redundancy/Failover – Never miss a call</li>
  </ul>

  <div class="contact">Phone: (13) 0044 7816<br>E-mail: info@norvane.net.au<br>Website: www.norvane.net.au</div>
</section>

<section class="page page--back">
  <svg class="page-art" viewBox="0 0 619 876" preserveAspectRatio="none">
    <defs>
      <linearGradient id="net-back" x1="0" y1="0" x2="1" y2="1">
        <stop offset="0" stop-color="#1a5fd0"/><stop offset=".5" stop-color="#2f8fe6"/><stop offset="1" stop-color="#0d3fae"/>
      </linearGradient>
    </defs>
    <g role="img" aria-label="Illustration: glowing global network">
      <path d="M0 0 H619 V225 Q430 275 260 268 Q110 258 0 195 Z" fill="url(#net-back)"/>
    </g>
    <path d="M318 0 Q332 178 560 248 Q600 252 619 246 V0 Z" fill="#4aa6dc"/>
    <path d="M334 0 Q348 162 560 236 Q600 242 619 236 V0 Z" fill="var(--sky)"/>
    <rect x="284" y="61" width="335" height="95" fill="#d4ecf8" opacity=".9"/>
    <circle cx="520" cy="260" r="250" fill="none" stroke="#fff" stroke-width="1" opacity=".5"/>
    <path d="M0 784 H330 Q405 784 412 841 H300 L282 876 H0 Z" fill="var(--grey)"/>
    <path d="M300 841 H619 V872 H284 Z" fill="var(--band)"/>
  </svg>

  <div class="brand"><div class="brand-name">norvane</div><div class="brand-tagline">Internet-Telephone-Security-Networking</div></div>

  <h2 class="section-title benefits-title">Benefits</h2>
  <ul class="bullets benefits-a">
    <li>No expensive onsite telephone equipment</li><li>Easily scale up or down and needs change</li><li>Free telephone/email support</li>
  </ul>
  <ul class="bullets benefits-b">
    <li>Lower monthly cost</li><li>Increase reliability</li><li>Easy self-administration</li>
  </ul>

  <table class="plans">
    <tr><td class="col-service">Service</td><td class="col-month">Monthly</td><td class="col-term">12 month term</td><td class="col-term-wide">24 month term</td><td class="col-term-wide">36 month term</td></tr>
    <tr><td>1Phone service only (phone sold separately)</td><td>$21.95</td><td></td><td></td><td></td></tr>
    <tr><td>Service + 2Corvell C20 Phone</td><td></td><td>$24.95</td><td>$22.95</td><td>$20.95</td></tr>
  </table>

  <div class="notes">
    <p>1For monthly service you may purchase the Corvell C20 phone for $65 each,<br>less taxes and shipping.</p>
    <p>2Corvell C20 phones are rented and due upon cancellation. Customer pays return shipping.</p>
  </div>

  <p class="savings">Save up to 40%!</p>

  <div class="contact">Phone: (13) 0044 7816<br>E-mail: info@norvane.net.au<br>Website: www.norvane.net.au</div>
</section>

</body>
</html>
```